Chatterly Now Hiring Post - Automotive Mechanics

1080 x 1080 design Chatterly ad post that we are hiring. Text to include:

We are hiring mechanics to perform suspension, brake, clutch and steering repairs on heavy duty trucks, trailers, busses and motorhomes.
Hourly wages plus performance bonus
Crestpoint Health Alliance Heath Care + Dental
401K + Company Match
Weekly Pay
3:00 pm – 11:00 pm Shift – No Weekends
Stop in anytime at Ridgeline Coil Works 5172 Heron Lane, Saginaw, MI 48601
or call 989-555-0187
email you resume to coilworks@ridgelinecoil.example

Target Market(s)

Automotive mechanics / Technicians

Industry/Entity Type

Automotive

Font styles to use
Sans Serif

Colors
0054AA
0677BA
7BADD7
CADEEF
E8F1F8

Requirements
Must have
• Must include the text, our logo, and picture from our service department file = ridgeline-coil-works-service.jpg
Nice to have
• Something similar to the same Pember Motor repair ad I attached
Should not have
• No images of people. The image that we provided is from our repair shop, we would like that one used.

```html
<!DOCTYPE html>
<html lang="en">
<head>
<meta charset="utf-8">
<title>Ridgeline Coil Works – We Are Hiring Mechanics</title>
<link href="https://fonts.googleapis.com/css2?family=Great+Vibes&family=Montserrat:wght@800;900&family=Dosis:wght@500;600&family=Inter:wght@400;500;600;700&display=swap" rel="stylesheet">
<style>
  :root {
    --navy: #0054AA;
    --blue: #0677BA;
    --sky: #7BADD7;
    --mist: #CADEEF;
    --ice: #E8F1F8;
    --accent: #3A9BEA;
    --yellow: #F6BF26;
    --black: #020202;
    --white: #FFFFFF;
    --silver: #D6D6D6;
    --rule: #1E7FCC;
  }
  * { margin: 0; padding: 0; box-sizing: border-box; }
  html, body { width: 1200px; height: 1200px; overflow: hidden; background: var(--black); }
  .poster {
    position: relative;
    width: 1200px;
    height: 1200px;
    background: var(--black);
    font-family: "Inter", Arial, sans-serif;
    color: var(--white);
    overflow: hidden;
  }
  .backdrop { position: absolute; inset: 0; }
  .brand {
    position: absolute;
    left: 62px;
    top: 68px;
    display: flex;
    align-items: center;
    gap: 16px;
  }
  .brand-mark { width: 34px; height: 34px; background: var(--white); }
  .brand-name {
    font-family: "Inter", Arial, sans-serif;
    font-weight: 700;
    font-size: 30px;
    letter-spacing: 0.5px;
    color: var(--white);
  }
  .headline { position: absolute; left: 630px; top: 30px; width: 560px; }
  .headline-script {
    font-family: "Great Vibes", cursive;
    font-size: 118px;
    line-height: 1;
    color: var(--white);
    position: absolute;
    left: 0;
    top: 0;
    z-index: 2;
  }
  .headline-main {
    position: absolute;
    left: 0;
    top: 82px;
    font-family: "Montserrat", Arial, sans-serif;
    font-weight: 900;
    font-size: 124px;
    line-height: 1;
    color: var(--yellow);
    letter-spacing: 1px;
  }
  .headline-sub {
    position: absolute;
    left: 130px;
    top: 220px;
    font-family: "Montserrat", Arial, sans-serif;
    font-weight: 800;
    font-size: 62px;
    line-height: 1;
    color: var(--silver);
    letter-spacing: 1px;
  }
  .intro {
    position: absolute;
    left: 58px;
    top: 270px;
    width: 430px;
    font-family: "Dosis", Arial, sans-serif;
    font-weight: 600;
    font-size: 29px;
    line-height: 42px;
    color: var(--mist);
  }
  .benefits { position: absolute; left: 44px; top: 500px; width: 410px; list-style: none; }
  .benefit {
    display: flex;
    align-items: center;
    gap: 26px;
    border-bottom: 1.5px solid var(--rule);
    font-size: 19px;
    line-height: 27px;
    color: var(--white);
  }
  .benefit:nth-child(1) { height: 92px; }
  .benefit:nth-child(2) { height: 91px; }
  .benefit:nth-child(3) { height: 93px; }
  .benefit:nth-child(4) { height: 86px; }
  .benefit:nth-child(5) { height: 96px; }
  .benefit-icon { width: 42px; height: 42px; flex: none; }
  .contact-call { position: absolute; left: 44px; top: 1046px; }
  .contact-label { font-weight: 700; font-size: 18px; letter-spacing: 0.3px; }
  .contact-phone {
    font-family: "Inter", Arial, sans-serif;
    font-weight: 700;
    font-size: 52px;
    line-height: 1.1;
    color: var(--accent);
    margin-left: -4px;
  }
  .contact-visit { position: absolute; left: 476px; top: 1023px; }
  .contact-visit .contact-label { font-weight: 500; font-size: 18px; }
  .contact-detail {
    font-family: "Dosis", Arial, sans-serif;
    font-weight: 600;
    font-size: 25px;
    color: var(--accent);
    margin-top: 6px;
    margin-bottom: 18px;
  }
</style>
</head>
<body>
<main class="poster">
  <svg class="backdrop" width="1200" height="1200" viewBox="0 0 1200 1200">
    <defs>
      <linearGradient id="bandGrad" x1="0" y1="0" x2="1" y2="0">
        <stop offset="0" stop-color="#0A1A30"/>
        <stop offset="0.55" stop-color="#0C3F80"/>
        <stop offset="1" stop-color="#0054AA"/>
      </linearGradient>
      <linearGradient id="shopGrad" x1="0" y1="0" x2="1" y2="1">
        <stop offset="0" stop-color="#A9A7A2"/>
        <stop offset="0.45" stop-color="#5E5B55"/>
        <stop offset="0.8" stop-color="#3C3935"/>
        <stop offset="1" stop-color="#6E6B66"/>
      </linearGradient>
      <linearGradient id="edgeGlow" x1="0" y1="0" x2="1" y2="0">
        <stop offset="0" stop-color="#FFFFFF" stop-opacity="0"/>
        <stop offset="0.5" stop-color="#FFFFFF" stop-opacity="0.9"/>
        <stop offset="1" stop-color="#FFFFFF" stop-opacity="0"/>
      </linearGradient>
    </defs>
    <polygon class="brand-band" points="0,0 578,0 545,183 0,183" fill="url(#bandGrad)"/>
    <polygon class="shop-photo" role="img" aria-label="Service department photo: heavy duty truck axles on stands with brake shoes and hubs exposed in the repair shop" points="517,311 1200,311 1200,983 383,983" fill="url(#shopGrad)"/>
    <polygon class="photo-edge" points="510,311 522,311 388,983 376,983" fill="url(#edgeGlow)" opacity="0.7"/>
  </svg>

  <div class="brand">
    <span class="brand-mark"></span>
    <span class="brand-name">Ridgeline Coil Works</span>
  </div>

  <h1 class="headline">
    <span class="headline-script">We Are</span>
    <span class="headline-main">HIRING</span>
    <span class="headline-sub">MECHANICS</span>
  </h1>

  <p class="intro">We are hiring mechanics to perform suspension, brake, clutch and steering repairs on heavy duty trucks, trailers, busses and motorhomes.</p>

  <ul class="benefits">
    <li class="benefit">
      <svg class="benefit-icon" viewBox="0 0 42 42" fill="none" stroke="#3A9BEA" stroke-width="2" stroke-linejoin="round">
        <rect x="4" y="14" width="34" height="22" rx="2"/>
        <path d="M4 16 L21 28 L38 16"/>
        <rect x="11" y="5" width="20" height="13" rx="1"/>
        <circle cx="21" cy="11" r="3"/>
      </svg>
      <span>Hourly wages plus<br>performance bonus</span>
    </li>
    <li class="benefit">
      <svg class="benefit-icon" viewBox="0 0 42 42" fill="none" stroke="#3A9BEA" stroke-width="2" stroke-linejoin="round" stroke-linecap="round">
        <path d="M21 4 L36 10 V20 C36 29 29 35 21 38 C13 35 6 29 6 20 V10 Z"/>
        <path d="M14 21 L19 26 L28 16"/>
      </svg>
      <span>Crestpoint Health Alliance Heath<br>Care + Dental</span>
    </li>
    <li class="benefit">
      <svg class="benefit-icon" viewBox="0 0 42 42" fill="none" stroke="#3A9BEA" stroke-width="2" stroke-linejoin="round">
        <path d="M8 12 L28 5 L31 12"/>
        <rect x="4" y="12" width="34" height="24" rx="3"/>
        <rect x="26" y="20" width="12" height="8" rx="2"/>
        <circle cx="31" cy="24" r="1.3" fill="#3A9BEA"/>
      </svg>
      <span>401K + Company Match</span>
    </li>
    <li class="benefit">
      <svg class="benefit-icon" viewBox="0 0 42 42" fill="none" stroke="#3A9BEA" stroke-width="2" stroke-linejoin="round">
        <rect x="4" y="7" width="34" height="31" rx="2"/>
        <path d="M4 15 H38 M12 3 V10 M30 3 V10"/>
        <path d="M10 21 h3 M17 21 h3 M24 21 h3 M31 21 h2 M10 27 h3 M17 27 h3 M24 27 h3 M31 27 h2 M10 33 h3 M17 33 h3 M24 33 h3" stroke-width="2.5"/>
      </svg>
      <span>Weekly Pay</span>
    </li>
    <li class="benefit">
      <svg class="benefit-icon" viewBox="0 0 42 42" fill="none" stroke="#3A9BEA" stroke-width="2" stroke-linecap="round">
        <circle cx="21" cy="21" r="17"/>
        <path d="M21 10 V21 L28 26"/>
      </svg>
      <span>3:00 pm – 11:00 pm Shift<br>No Weekends</span>
    </li>
  </ul>

  <div class="contact-call">
    <p class="contact-label">CALL FOR MORE INFO.</p>
    <p class="contact-phone">989-555-0187</p>
  </div>

  <div class="contact-visit">
    <p class="contact-label">STOP IN ANYTIME @</p>
    <p class="contact-detail">Ridgeline Coil Works 5172 Heron Lane, Saginaw, MI 48601</p>
    <p class="contact-label">Email Your Resume :</p>
    <p class="contact-detail">coilworks@ridgelinecoil.example</p>
  </div>
</main>
</body>
</html>
```